pathology learning flashcard template graphic design .

Creative designs for 2 sides of the flashcards to include colorful sectioning and font sizes that will make it easy to use in studying.

```html
<!DOCTYPE html>
<html lang="en">
<head>
<meta charset="UTF-8">
<title>Pathology Flashcard – Case 0001</title>
<link href="https://fonts.googleapis.com/css2?family=Itim&display=swap" rel="stylesheet">
<style>
  :root {
    --page-bg: #e3e3e3;
    --card-top: #5fd8f2;
    --card-mid: #b9eef9;
    --card-bottom: #ffffff;
    --navy: #0d4a7a;
    --label-blue: #1d6aa6;
    --ink: #111820;
    --portrait-a: #f4e3d3;
    --portrait-b: #3f8a5e;
  }
  * { box-sizing: border-box; margin: 0; padding: 0; }
  html, body { width: 1200px; height: 800px; overflow: hidden; }
  body {
    background: var(--page-bg);
    font-family: "Itim", sans-serif;
    color: var(--ink);
    position: relative;
  }
  .card {
    position: absolute;
    top: 29px;
    width: 446px;
    height: 742px;
    border-radius: 6px;
    background: linear-gradient(180deg, var(--card-top) 0%, var(--card-mid) 35%, var(--card-bottom) 62%);
    box-shadow: 0 2px 5px rgba(0,0,0,0.25);
    overflow: hidden;
  }
  .card--front { left: 129px; }
  .card--back { left: 634px; background: linear-gradient(180deg, #bdf0fb 0%, #e4f8fd 45%, #ffffff 60%); }

  .tab {
    position: absolute;
    left: 0;
    background: var(--navy);
    color: #fff;
    clip-path: polygon(0 0, 100% 0, 95% 100%, 0 100%);
    display: flex;
    align-items: center;
  }
  .tab--case { top: 21px; width: 289px; height: 42px; padding-left: 13px; font-size: 22px; letter-spacing: 0.5px; }
  .tab--answer { top: 341px; width: 190px; height: 34px; padding-left: 13px; font-size: 21px; letter-spacing: 0.5px; }

  .portrait {
    position: absolute;
    left: 133px; top: 83px;
    width: 180px; height: 227px;
    border: 3px solid var(--navy);
    border-radius: 10px;
    background: linear-gradient(180deg, #ffffff 0%, var(--portrait-a) 55%, var(--portrait-b) 100%);
  }

  .case-text {
    position: absolute;
    left: 13px; top: 340px;
    width: 420px;
    font-size: 17.6px;
    line-height: 21.6px;
    text-align: justify;
    text-align-last: left;
  }
  .options {
    position: absolute;
    left: 14px; top: 654px;
    width: 420px;
    display: grid;
    grid-template-columns: 198px 1fr;
    row-gap: 7px;
    font-size: 17.6px;
    line-height: 22px;
  }
  .options__letter { color: var(--label-blue); }

  .diagnosis-title {
    position: absolute;
    top: 47px; left: 0; width: 100%;
    text-align: center;
    color: var(--navy);
    font-size: 36px;
    letter-spacing: 1px;
  }
  .section-label {
    position: absolute;
    left: 14px;
    color: var(--label-blue);
    font-size: 16.5px;
    letter-spacing: 0.3px;
  }
  .section-text {
    position: absolute;
    left: 14px;
    width: 425px;
    font-size: 13.8px;
    line-height: 21.6px;
  }
  .label--definition { top: 115px; }
  .text--definition { top: 139px; }
  .label--symptoms { top: 209px; }
  .text--symptoms { top: 233px; }

  .explanation {
    position: absolute;
    left: 14px; top: 400px;
    width: 418px;
    font-size: 17.6px;
    line-height: 22.8px;
    letter-spacing: 0.3px;
    text-align: justify;
    text-align-last: left;
  }
</style>
</head>
<body>
  <section class="card card--front">
    <div class="tab tab--case">Pathology Case ID 0001</div>
    <div class="portrait" role="img" aria-label="Cartoon illustration of an elderly patient"></div>
    <p class="case-text">50-year-old woman comes to the clinic because she has difficulty swallowing for the past few months. She says symptoms have been worsening. She also complains of cough, mostly at night and in fear of choking, has stopped eating many foods, losing about 12 lbs in the past 3 months. Past medical history is unremarkable. Vital signs are normal and physical exam is unremarkable. Chest x-ray with demonstrates an air-fluid level, while manometry shows absent relaxation of the lower esophageal sphincter during swallowing. What is the most likely diagnosis?</p>
    <div class="options">
      <div><span class="options__letter">A)</span> GERD</div>
      <div><span class="options__letter">C)</span> Achalasia</div>
      <div><span class="options__letter">B)</span> Barret Esophagus</div>
      <div><span class="options__letter">D)</span> Eosinophilic esophagitis</div>
    </div>
  </section>

  <section class="card card--back">
    <h1 class="diagnosis-title">ACHALASIA</h1>
    <h2 class="section-label label--definition">Definition:</h2>
    <p class="section-text text--definition">•Motility disorder where esophageal relaxation is impaired in the lower esophageal sphincter (LES).</p>
    <h2 class="section-label label--symptoms">P/E and Symptoms:</h2>
    <p class="section-text text--symptoms">•Dysphagia that is progressive, regurgitation, weight-loss, dry cough, chest pain, GERD, esophageal perforation, squamous cell carcinoma, aspiration pneumonia.</p>
    <div class="tab tab--answer">C - Achalasia</div>
    <p class="explanation">Symptoms and studies suggestive of achalasia. Patient’s manometry presents with no relaxation of the lower esophageal sphincter during swallowing. Patient also complains of dysphagia and is unable to swallow properly, leading to weight loss. Patient has no past infection or inflammation, ruling out eosinophilic esophagitis. Patient does not have chronic GERD, eliminating the possibility of Barrett esophagus, in which at least 5 years of acid reflux are beforehand to develop columnar metaplasia.</p>
  </section>
</body>
</html>
```